Brisk Lantern Estates, which offers a selection of prime properties (villas

A website that contains: Idea, benefits, destinations (villas), offers, about us, contact, newsletter, social media, blog, look at the attachment, even if it is in German. The idea is that I can easily add new pages, if necessary, with the design you make. Later on we want to add a reservation system, so you can book your villa through the internet. Besides, there is a concierge service available, which organizes everything for the customer, owner, from villa to restaurant, limo service, ... & benefits and emotions through nice pictures / videos, they should be convinced to invest.

Target Market(s)

Investors (golfer and non-golfer) which have 300'000 to invest in a kind of real-estate investing club

Number of Pages Required

5+ page

Font styles to use
Sans Serif

Requirements
Must have
• It must be for wordpress, must have an exclusive touch, high quality, with nice pictures of golf courses. The Logo is gold so it has to match with gold, the font is segan or segoe semilight or similar, sans serif
Nice to have
• may be as well as the possibility to include videos of the different destinations and houses

```html
<!DOCTYPE html>
<html lang="en">
<head>
<meta charset="utf-8">
<title>Brisk Lantern Estates</title>
<link rel="stylesheet" href="https://fonts.googleapis.com/css2?family=Open+Sans:wght@300;400;600&family=Great+Vibes&display=swap">
<style>
:root{
  --black:#000;
  --gold:#e0a72a;
  --gold-deep:#8a6410;
  --gold-soft:#d9ad4a;
  --ink:#ffffff;
  --muted:#9a9a9a;
  --paper:#f2f2f2;
  --canvas:#ffffff;
}
*{margin:0;padding:0;box-sizing:border-box}
html,body{width:1200px;height:1200px;overflow:hidden;background:var(--canvas)}
body{font-family:"Open Sans",sans-serif;font-weight:300;color:var(--ink)}
.page{position:absolute;left:411px;top:1.6px;width:470px;height:1498px;background:var(--black);transform:scale(.8);transform-origin:0 0;overflow:hidden}
.abs{position:absolute}
.script{font-family:"Great Vibes",cursive;font-weight:400}
.tiny{font-size:3.6px;line-height:5.8px;color:var(--muted)}
/* header */
.header{left:0;top:0;width:470px;height:32px;background:var(--black)}
.brand{left:56px;top:20px;font-size:5.5px;color:var(--gold);letter-spacing:.2px}
.brand-mark{left:84px;top:5px;width:14px;height:13px;border:1px solid var(--gold)}
.nav{left:152px;top:14px;display:flex;gap:12px;font-size:4.3px;color:#ddd}
.nav-active{left:152px;top:0;width:30px;height:34px;background:var(--gold);clip-path:polygon(0 0,100% 0,100% 88%,50% 100%,0 88%)}
.social{left:364px;top:16px;display:flex;gap:2px}
.social span{width:7px;height:7px;border-radius:50%;background:#fff;display:block}
/* hero */
.hero{left:0;top:32px;width:470px;height:290px;background:linear-gradient(180deg,#d6c58e 0%,#b59a5c 35%,#6f6a3a 65%,#000 100%)}
.hero-box{left:195px;top:124px;width:189px;height:79px;background:rgba(150,150,150,.6)}
.hero-title{left:0;top:148px;width:470px;text-align:center;font-size:28px;font-weight:300;color:#fff;text-shadow:0 1px 3px rgba(0,0,0,.4)}
.hero-btn{left:168px;top:193px;width:134px;height:20px;background:#000;font-size:4px;font-weight:600;text-align:center;line-height:20px;color:#fff}
/* about */
.about{left:58px;top:266px;width:96px;height:318px;background:var(--paper)}
.about-logo{left:8px;top:10px;width:80px;height:72px;border:1px solid var(--gold);color:var(--gold);font-size:6px;text-align:center;padding-top:50px}
.about-script{left:4px;top:100px;font-size:30px;color:#333}
.principle{left:0;top:147px;width:96px;height:27px;background:var(--gold);font-size:10px;color:#fff;padding:6px 4px}
.about-text{left:5px;top:184px;width:86px;color:#888}
/* offer cards */
.card-img{top:266px;width:84px;height:80px}
.card-title{top:351px;font-size:8.5px;color:#ddd}
.card-text{top:364px;width:78px}
.card-btn{top:415px;width:84px;height:15px;background:var(--gold);font-size:4px;color:#fff;padding:5px 4px}
/* video */
.video{left:157px;top:434px;width:254px;height:150px;background:linear-gradient(180deg,#5b6066 0%,#7d8280 45%,#4b5a2e 100%)}
.play{left:121px;top:68px;width:12px;height:12px;border:1px solid #fff;border-radius:50%}
/* newsletter */
.newsletter{left:58px;top:589px;width:353px;height:63px;background:linear-gradient(180deg,#d2a544,#e0b14a 60%,#c9962d)}
.news-title{left:0;top:6px;width:353px;text-align:center;font-size:10px;color:#fff}
.news-input{left:46px;top:40px;width:184px;height:10px;border-bottom:1px solid rgba(255,255,255,.7);font-size:4px;padding:3px 6px}
.news-btn{left:230px;top:34px;width:80px;height:16px;background:#fff;color:#555;font-size:4px;text-align:center;line-height:16px}
/* offers */
.section-script{left:0;width:470px;text-align:center;font-size:22px;color:#ccc}
.offer-title{font-size:17px;line-height:15px;color:var(--gold)}
.offer-box{background:var(--gold);padding:12px 11px}
.offer-box p{font-size:5px;line-height:8px;color:#fff}
.offer-box p.lead{font-weight:600;margin-bottom:8px}
.offer-btn{width:75px;height:20px;background:var(--gold-deep);color:#f3e0b0;font-size:5px;text-align:center;line-height:20px}
/* blogs */
.blog{top:1175px;width:115px;height:162px;border:1px solid #222}
.blog-img{left:0;top:0;width:113px;height:103px}
.blog-text{left:5px;top:112px;width:104px}
.blog-more{left:5px;top:146px;font-size:3.8px;font-weight:600;color:var(--gold)}
/* contact */
.rule{left:58px;top:1359px;width:353px;height:1px;background:#333}
.contact-title{left:58px;top:1366px;font-size:8px;color:#bbb}
.map{left:58px;top:1392px;width:126px;height:58px;background:linear-gradient(135deg,#eeeeee,#d9dbde)}
.info{left:186px;top:1376px;width:225px;height:90px;border:1px solid #333}
.info .tiny{color:#aaa}
.icon{width:6px;height:6px}
/* footer */
.footer-copy{left:58px;top:1490px;font-size:3.5px;color:#888}
.footer-social{left:364px;top:1489px;display:flex;gap:2px}
.footer-social span{width:6px;height:6px;border-radius:50%;border:1px solid #999;display:block}
</style>
</head>
<body>
<div class="page">
  <header class="abs header">
    <div class="abs brand-mark"></div>
    <div class="abs brand">BRISK LANTERN ESTATES</div>
    <div class="abs nav-active"></div>
    <nav class="abs nav" style="left:162px"><span>Idea</span><span>Benefits</span><span>Destinations</span><span>Offers</span><span>About us</span><span>Blog</span><span>Contact</span>
      <svg width="6" height="6" viewBox="0 0 6 6"><circle cx="2.5" cy="2.5" r="1.8" fill="none" stroke="#ddd" stroke-width=".6"/><line x1="3.8" y1="3.8" x2="5.6" y2="5.6" stroke="#ddd" stroke-width=".6"/></svg>
    </nav>
    <div class="abs social"><span></span><span></span><span></span><span></span><span></span></div>
  </header>

  <section class="abs hero" role="img" aria-label="Mediterranean villa with palm trees and a pool at sunset"></section>
  <div class="abs hero-box"></div>
  <h1 class="abs hero-title" style="font-weight:300">Reach New Heights</h1>
  <div class="abs hero-btn">INVEST ON US TO REACH THE POSSIBILITIES</div>

  <aside class="abs about">
    <div class="abs about-logo">BRISK LANTERN ESTATES</div>
    <div class="abs about-script script">About us</div>
    <div class="abs principle">Principle</div>
    <p class="abs about-text tiny">As an investor, you become a member of the owners club, which manages the shared use of every property. The concierge service takes care of each stay, from arrival to the last dinner. Every member receives a fair share of weeks in the year, planned in advance and balanced between seasons. Unused weeks can be passed on to friends and family or returned to the club for credit. A monthly fee covers upkeep, staff and the garden, so each villa stays ready for you at all times. Additional weeks may be booked when free.<br><br>READ MORE</p>
  </aside>

  <div class="abs card-img" style="left:157px;background:linear-gradient(180deg,#3f7fc4,#4a8a4a 55%,#2fb3c4)" role="img" aria-label="Tropical island with mountain and overwater bungalows"></div>
  <div class="abs card-img" style="left:243px;background:linear-gradient(180deg,#c9d3d6,#8a9a6a 55%,#d8d4c8)" role="img" aria-label="Open pavilion with daybed overlooking the sea"></div>
  <div class="abs card-img" style="left:328px;background:linear-gradient(180deg,#3c86d8,#c79a55 55%,#3e7a35)" role="img" aria-label="Vintage villa with terraces and garden"></div>
  <div class="abs card-title" style="left:161px">Moutain Island</div>
  <div class="abs card-title" style="left:246px">Peace of City</div>
  <div class="abs card-title" style="left:331px">Vintage talks</div>
  <p class="abs card-text tiny" style="left:161px">Quiet villa near the coast with views over the bay, private terrace and pool for long, slow summer days.</p>
  <p class="abs card-text tiny" style="left:246px">Quiet villa near the coast with views over the bay, private terrace and pool for long, slow summer days.</p>
  <p class="abs card-text tiny" style="left:331px">Quiet villa near the coast with views over the bay, private terrace and pool for long, slow summer days.</p>
  <div class="abs card-btn" style="left:157px">Offer Details</div>
  <div class="abs card-btn" style="left:243px">Offer Details</div>
  <div class="abs card-btn" style="left:328px">Offer Details</div>

  <div class="abs video" role="img" aria-label="Video still of luxury cars parked on a lawn by a lake">
    <div class="abs" style="left:4px;top:8px;font-size:6px;color:#fff">See all videos</div>
    <div class="abs" style="left:230px;top:9px;font-size:4px;color:#fff">View all</div>
    <div class="abs play"><svg width="10" height="10" viewBox="0 0 10 10" style="position:absolute;left:0;top:0"><polygon points="4,3 7.5,5 4,7" fill="#fff"/></svg></div>
  </div>

  <section class="abs newsletter" role="img" aria-label="Golden city skyline at dusk">
    <div class="abs news-title">Subscribe Our Newsletter</div>
    <div class="abs news-input">Email</div>
    <div class="abs news-btn">SUBSCRIBE</div>
  </section>

  <div class="abs section-script script" style="top:670px">Offers</div>

  <div class="abs" style="left:58px;top:699px;width:190px;height:212px;background:linear-gradient(180deg,#3d78c8 0%,#bcd3e6 35%,#6a7a3e 60%,#3d9aa6 100%)" role="img" aria-label="Resort pool with palm trees and thatched pavilion"></div>
  <div class="abs offer-title" style="left:258px;top:760px">Ihr Nutzen –<br>emotional</div>
  <div class="abs offer-box" style="left:248px;top:788px;width:163px;height:123px">
    <p class="lead">Sie sind Mitbesitzer von exklusiven Immobilien in Topresorts, in wunderschöner, gepflegter und sicherer Umgebung</p>
    <p>Miteigentum ermöglicht Ihnen, Ihre Ferien an verschiedenen Destinationen zu verbringen – Abwechslung ist garantiert<br>Sie geniessen</p>
  </div>
  <div class="abs offer-btn" style="left:258px;top:883px">Know more</div>

  <div class="abs offer-title" style="left:70px;top:968px">Ihr Nutzen -<br>praktisch</div>
  <div class="abs offer-box" style="left:58px;top:999px;width:164px;height:124px">
    <p class="lead">Sie sind Mitbesitzer von exklusiven Immobilien in Topresorts, in wunderschöner, gepflegter und sicherer Umgebung</p>
    <p>Miteigentum ermöglicht Ihnen, Ihre Ferien an verschiedenen Destinationen zu verbringen – Abwechslung ist garantiert<br>Sie geniessen</p>
  </div>
  <div class="abs offer-btn" style="left:70px;top:1095px">Know more</div>
  <div class="abs" style="left:222px;top:911px;width:189px;height:212px;background:linear-gradient(180deg,#3a4150 0%,#8d7a78 35%,#3c3a35 60%,#3f6b2c 100%)" role="img" aria-label="Stone villa at dusk with lit garden path"></div>

  <div class="abs section-script script" style="top:1140px">Blogs</div>

  <article class="abs blog" style="left:58px">
    <div class="abs blog-img" style="background:linear-gradient(180deg,#6b86b0,#8a7a62 60%,#555)" role="img" aria-label="Limousine in front of a grand hotel"></div>
    <p class="abs blog-text tiny">A short story from our members about arriving in style, a quiet hotel stay and the first round of the week.</p>
    <div class="abs blog-more">READ MORE</div>
  </article>
  <article class="abs blog" style="left:177px">
    <div class="abs blog-img" style="background:linear-gradient(180deg,#3f5c9c,#d9889a 50%,#4f5a48)" role="img" aria-label="Beachfront resort tower at sunset"></div>
    <p class="abs blog-text tiny">A short story from our members about arriving in style, a quiet hotel stay and the first round of the week.</p>
    <div class="abs blog-more">READ MORE</div>
  </article>
  <article class="abs blog" style="left:296px">
    <div class="abs blog-img" style="background:linear-gradient(180deg,#5d8ac8,#d8c24a 55%,#3b4a5a)" role="img" aria-label="Modern cube houses in yellow and grey"></div>
    <p class="abs blog-text tiny">A short story from our members about arriving in style, a quiet hotel stay and the first round of the week.</p>
    <div class="abs blog-more">READ MORE</div>
  </article>

  <div class="abs rule"></div>
  <div class="abs contact-title">Contact us</div>
  <div class="abs map" role="img" aria-label="Street map showing the office location"></div>
  <div class="abs info">
    <div class="abs tiny" style="left:24px;top:16px">INFORMATIONEN UND ANMELDUNG</div>
    <div class="abs tiny" style="left:24px;top:29px;color:#ddd">Brisk Lantern Estates<br>c/o Fairway Circle Group GmbH<br>Lindenweg 12<br>CH-8000 Zürich<br>Zürich / Switzerland</div>
    <svg class="abs icon" style="left:106px;top:33px" viewBox="0 0 6 6"><path d="M1 .5 L2.2 .5 L2.6 2 L1.9 2.5 Q2.7 3.6 3.5 4.1 L4 3.4 L5.5 3.8 L5.5 5 Q2 5.2 1 .5Z" fill="var(--gold)"/></svg>
    <div class="abs tiny" style="left:117px;top:33px;color:#ddd">+41 00 555 01 20<br>+41 00 555 01 21</div>
    <svg class="abs icon" style="left:106px;top:50px" viewBox="0 0 6 6"><rect x=".5" y="1.2" width="5" height="3.6" fill="var(--gold)"/><path d="M.5 1.2 L3 3.2 L5.5 1.2" fill="none" stroke="#000" stroke-width=".5"/></svg>
    <div class="abs tiny" style="left:117px;top:50px;color:#ddd">info@fairwaycircle.example</div>
    <div class="abs tiny" style="left:24px;top:66px;width:195px">Please contact us for a personal meeting, we gladly answer all your questions.<br>Your Brisk Lantern Team</div>
  </div>

  <div class="abs footer-copy">©Brisk Lantern Estates | 2024</div>
  <div class="abs footer-social"><span></span><span></span><span></span><span></span><span></span></div>
</div>
</body>
</html>
```